Willow Ascent Services Business Card Design

I require a business card design for my business Willow Ascent Services. The purpose of this business is to enable people to make positive change in their lives. This business offers life coaching, hypnotherapy and facilitation services. The slogan is 'Grow past the old and shape the life you want.' Coaching services will be available internationally whilst the hypnotherapy and facilitation services will focus on delivery in south east Queensland.

The business card should be crisp, clean, professional and give the client positive feelings of achieving success.

The logo must be representative of a phoenix rising from the ashes which is a symbol of regeneration and new life. My preference is a black Phoenix on a white background similar to the Phoenix image attached to this brief. I'm happy to see other concepts you have too. The logo and business name must be scalable so it can be printed on a large outdoor sign. Therefore the following files must be provided as a minimum:
-Business card
-Logo on it's own
-Business name on it's own

The following detail must appear on either the front/back of the business card
-Logo
-Willow Ascent Services
-Grow past the old and shape the life you want.
-Personal and business success through
-Coaching | Hypnotherapy | Facilitation
-Greta Halloway
-Founder

-Life Coach
-Clinical Hypnotherapist
-MBA (Project Management specialisation)
-Neuro Linguistic Programming Practitioner

-0412 835 076
-E: willowascent.au@kestrelmail.com
-www.willow-ascent.com.au
-Contact us now for your free 20min assessment

Please feel free to ask me as many questions as you like :) Thank you.

Hi all,  friendly reminder that the logo needs to be your own design and cannot be a Framequarry or other purchased or free image.  

Thanks heaps
Keep the great designs coming in. You're all so talented.
Greta

• Feedback from older people is that black backgrounds with lighter fonts are difficult to read so please no black backgrounds.

```html
<!DOCTYPE html>
<html lang="en">
<head>
<meta charset="utf-8">
<title>Willow Ascent Services – Business Card</title>
<link rel="stylesheet" href="https://fonts.googleapis.com/css2?family=Open+Sans:wght@400;600&display=swap">
<style>
  :root {
    --bg: #e9e9e9;
    --card: #ffffff;
    --ink: #3a3a3a;
    --muted: #6b6b6b;
    --rule: #8a8a8a;
    --orange: #f07d1a;
  }
  * { box-sizing: border-box; margin: 0; padding: 0; }
  html, body { width: 1200px; height: 1200px; overflow: hidden; }
  body {
    background: var(--bg);
    font-family: "Open Sans", Arial, sans-serif;
    color: var(--ink);
    position: relative;
  }
  .card {
    position: absolute;
    left: 180px;
    width: 840px;
    height: 480px;
    background: var(--card);
    box-shadow: 0 6px 24px rgba(0,0,0,.12);
    overflow: hidden;
  }
  .card--front { top: 90px; }
  .card--back { top: 630px; }

  .brand { position: absolute; display: flex; align-items: center; gap: 18px; }
  .brand__dot { width: 92px; height: 92px; border-radius: 50%; background: var(--orange); flex: none; }
  .brand__name { font-weight: 600; font-size: 34px; line-height: 1.1; color: var(--orange); white-space: nowrap; }

  .card--front .brand { left: 80px; top: 110px; }
  .slogan {
    position: absolute; left: 120px; top: 62px;
    font-size: 17px; color: var(--muted);
  }
  .front-info { position: absolute; left: 200px; top: 270px; width: 560px; list-style: none; }
  .front-info li { display: flex; align-items: center; gap: 14px; font-size: 21px; line-height: 1.55; color: var(--muted); }
  .front-info li::before { content: ""; width: 14px; height: 11px; background: var(--ink); border-radius: 2px; flex: none; }
  .front-info .rule { border-top: 1.5px solid var(--rule); margin: 6px 0 6px 28px; height: 0; }
  .front-info .rule::before { display: none; }

  .card--back .brand { left: 60px; top: 80px; }
  .card--back .brand__dot { width: 80px; height: 80px; }
  .card--back .brand__name { font-size: 28px; }
  .credentials { position: absolute; left: 440px; top: 56px; list-style: none; }
  .credentials li { font-size: 18px; line-height: 1.5; color: var(--muted); white-space: nowrap; }
  .credentials li::before { content: "•"; color: var(--ink); margin-right: 6px; }
  .back-rule { position: absolute; left: 440px; right: 40px; top: 186px; border-top: 1.5px solid var(--rule); }
  .contacts { position: absolute; left: 440px; top: 200px; list-style: none; }
  .contacts li { display: flex; align-items: center; gap: 12px; font-size: 21px; line-height: 1.6; color: var(--ink); white-space: nowrap; }
  .contacts svg { width: 24px; height: 24px; flex: none; }
  .offer {
    position: absolute; left: 0; bottom: 40px; width: 600px; height: 70px;
    background: var(--orange);
    clip-path: polygon(0 0, 100% 0, 94% 100%, 0 100%);
    display: flex; align-items: center; padding-left: 50px;
    font-size: 21px; color: var(--ink); white-space: nowrap;
  }
</style>
</head>
<body>
  <section class="card card--front" aria-label="Card front">
    <p class="slogan">'Grow past the old and shape the life you want.'</p>
    <div class="brand">
      <span class="brand__dot"></span>
      <span class="brand__name">Willow Ascent Services</span>
    </div>
    <ul class="front-info">
      <li>Personal and business success through</li>
      <li>Coaching | Hypnotherapy | Facilitation</li>
      <li class="rule"></li>
      <li>Greta Halloway</li>
      <li>Founder</li>
    </ul>
  </section>

  <section class="card card--back" aria-label="Card back">
    <div class="brand">
      <span class="brand__dot"></span>
      <span class="brand__name">Willow Ascent<br>Services</span>
    </div>
    <ul class="credentials">
      <li>Life Coach</li>
      <li>Clinical Hypnotherapist</li>
      <li>MBA (Project Management specialisation)</li>
      <li>Neuro Linguistic Programming Practitioner</li>
    </ul>
    <div class="back-rule"></div>
    <ul class="contacts">
      <li><svg viewBox="0 0 24 24"><circle cx="12" cy="12" r="12" fill="#f07d1a"/><rect x="8.5" y="5.5" width="7" height="13" rx="1.5" fill="#fff"/></svg>0412 835 076</li>
      <li><svg viewBox="0 0 24 24"><circle cx="12" cy="12" r="12" fill="#f07d1a"/><rect x="6" y="8" width="12" height="8" fill="#fff"/><path d="M6 8l6 5 6-5" fill="none" stroke="#f07d1a" stroke-width="1.3"/></svg>willowascent.au@kestrelmail.com</li>
      <li><svg viewBox="0 0 24 24"><circle cx="12" cy="12" r="12" fill="#f07d1a"/><circle cx="12" cy="12" r="6" fill="none" stroke="#fff" stroke-width="1.5"/><path d="M6 12h12M12 6c-3 3-3 9 0 12M12 6c3 3 3 9 0 12" fill="none" stroke="#fff" stroke-width="1.2"/></svg>www.willow-ascent.com.au</li>
    </ul>
    <div class="offer">Contact us now for your free 20min assessment</div>
  </section>
</body>
</html>
```